Web Design Project

Please take a look at my current aged website www.tarlowpeopleadvisory.com and my newly designed logo and business cards. I would like a new fresh updated look to my website and my new designs incorporated.
Updates

  Good Morning Everyone

Due to an Austrralian licencing issue I have had to have my logo slightly redesigned.

Would you please be able to look at the newly uploaded files and revise your designs.

Thanks so much.  I am very happy with the calibre and quality of the designs so far.

kind Regards

Marnie

Industry/Entity Type

Business

Requirements
Must have
• the exisiting pages and fresh new graphics and a real commitment to my palette of lime green, turqouise and black.

```html
<!DOCTYPE html>
<html lang="en">
<head>
<meta charset="utf-8">
<title>Tarlow HR Advisory</title>
<link href="https://fonts.googleapis.com/css2?family=Tinos:wght@400;700&family=Arimo:wght@400;700&family=Open+Sans:wght@400;600&display=swap" rel="stylesheet">
<style>
:root{
  --ink:#231f20;
  --lime:#5fb64a;
  --lime-light:#7cc95e;
  --lime-deep:#2f7d2a;
  --turquoise:#1aa6c9;
  --panel:#a7aaab;
  --card:#c4c4c4;
  --white:#ffffff;
  --orange:#ff8a00;
  --orange-deep:#ff4a0a;
}
*{box-sizing:border-box;margin:0;padding:0}
html,body{width:1200px;height:1176px;overflow:hidden;background:var(--white)}
.canvas{position:relative;width:1200px;height:1176px}
.abs{position:absolute}
.header{left:144px;top:48px;width:912px;height:166px;background:var(--ink);border-radius:8px;box-shadow:0 2px 4px rgba(0,0,0,.4)}
.brand{left:178px;top:82px;display:flex;align-items:center;gap:16px}
.brand-mark{width:100px;height:100px;border-radius:50%;border:6px solid var(--turquoise)}
.brand-name{font-family:'Arimo',sans-serif;font-weight:700;font-size:38px;color:var(--turquoise);line-height:1}
.brand-tag{font-family:'Arimo',sans-serif;font-weight:700;font-size:11px;color:var(--lime-light);margin-top:6px;letter-spacing:.3px}
.social{left:690px;top:30px;display:flex;gap:30px}
.social span{width:72px;height:72px;border-radius:50%;box-shadow:0 3px 6px rgba(0,0,0,.35)}
.s1{background:#eeeeee}.s2{background:var(--orange)}.s3{background:#1b4f8a}.s4{background:#3cbde8}
.search{left:684px;top:134px;width:350px;height:41px;border-radius:10px;background:#b5b5b5;display:flex;align-items:center;padding-left:14px;font-family:'Tinos',serif;font-weight:700;font-size:22px;color:#8a8a8a}
.search-field{position:absolute;left:100px;top:2px;right:2px;bottom:2px;background:var(--ink);border-radius:9px;border:2px solid #777}
.search-field::after{content:"";position:absolute;left:18px;top:8px;width:2px;height:22px;background:#ddd}
.nav{left:96px;top:222px;width:1008px;height:54px;background:var(--lime);border-radius:8px;box-shadow:0 2px 4px rgba(0,0,0,.35)}
.nav-tab{top:222px;height:54px;border-radius:8px;background:var(--lime-light);border:1px solid #3f8a33;font-family:'Tinos',serif;font-weight:700;font-size:29px;color:var(--ink);display:flex;align-items:center;justify-content:center}
.nav-tab.is-active{background:var(--turquoise)}
.content{left:144px;top:290px;width:912px;height:752px;background:var(--panel);border-radius:10px;box-shadow:0 2px 4px rgba(0,0,0,.4)}
.intro{left:156px;top:314px;width:488px;height:712px;background:var(--card);border-radius:10px;box-shadow:1px 2px 3px rgba(0,0,0,.6);text-align:center;padding-top:10px}
.intro h1{font-family:'Arimo',sans-serif;font-weight:700;font-size:21.5px;color:var(--ink)}
.intro p{font-family:'Tinos',serif;font-size:22.5px;line-height:29px;color:var(--ink);margin:0 auto 29px;width:440px}
.intro p:first-of-type{margin-top:2px}
.intro a{color:var(--turquoise)}
.quote{left:660px;top:316px;width:382px;height:320px;background:var(--ink);border-radius:10px;box-shadow:1px 2px 3px rgba(0,0,0,.6);color:var(--white);font-family:'Arimo',sans-serif;text-align:center;font-size:21px;line-height:18px;padding:12px 16px 0}
.quote cite{display:block;font-style:normal;font-weight:700;margin-top:18px}
.photo{left:708px;top:644px;width:300px;height:364px;background:linear-gradient(135deg,#f2f4f5,#6d7680 60%,#2a2f36)}
.footer{left:144px;top:1056px;width:424px;height:120px;background:var(--ink);border-radius:8px 0 0 0;text-align:center;font-family:'Open Sans',sans-serif;color:var(--white)}
.footer small{display:block;font-size:14px;margin-top:12px;margin-right:30px}
.footer nav{margin-top:34px;font-size:14px;margin-right:60px}
.footer nav a{color:var(--turquoise);text-decoration:none}
.promo{left:564px;top:1048px;width:496px;height:128px;background:linear-gradient(90deg,var(--orange),var(--orange-deep));border-radius:8px 8px 0 0;overflow:hidden}
.promo h2{position:absolute;left:52px;top:34px;font-family:'Open Sans',sans-serif;font-weight:400;font-size:29px;line-height:30px;color:var(--white);letter-spacing:-.5px}
.promo p{position:absolute;left:52px;top:98px;font-family:'Open Sans',sans-serif;font-size:13px;color:var(--white)}
.promo-accent{position:absolute;right:0;top:0;width:110px;height:128px;background:linear-gradient(90deg,var(--lime),var(--lime-deep))}
</style>
</head>
<body>
<div class="canvas">
  <header class="abs header"></header>
  <div class="abs brand">
    <span class="brand-mark"></span>
    <div>
      <div class="brand-name">Tarlow Advisory</div>
      <div class="brand-tag">Human Resources and Recruitment Solutions</div>
    </div>
  </div>
  <div class="abs social" aria-label="Social links">
    <span class="s1"></span><span class="s2"></span><span class="s3"></span><span class="s4"></span>
  </div>
  <div class="abs search">Search:<span class="search-field"></span></div>

  <nav class="abs nav"></nav>
  <div class="abs nav-tab is-active" style="left:144px;width:144px">Home</div>
  <div class="abs nav-tab" style="left:288px;width:206px">Our Services</div>
  <div class="abs nav-tab" style="left:494px;width:244px">Our Consultants</div>
  <div class="abs nav-tab" style="left:738px;width:146px">Our Fees</div>
  <div class="abs nav-tab" style="left:884px;width:172px">Contact Us</div>

  <main class="abs content"></main>
  <section class="abs intro">
    <h1>What can Tarlow HR Advisory do for me?</h1>
    <p>During these challenging economic times it can be difficult to justify internal human resources management services or support. However as a business owner or Manager you may find that HR support or advice is required from time to time.</p>
    <p>Tarlow HR Advisory are an outsourced HR function.&nbsp; We can provide you with that ongoing support, offer solutions and assist you with developing strategies that fit your business and deliver results.</p>
    <p>Take a look at <a href="#">Our Services</a> to see how our comprehensive consultancy can add value to your business.</p>
    <p>By outsourcing some or all of your HR function you will effectively manage your costs, be able to focus on your core business and still have access to professional up-to-date HR advice, systems and processes.</p>
  </section>
  <blockquote class="abs quote">“According to a recent survey by Harcourt Lane Partners more than 80% of companies outsource some type of task or project each year.&nbsp; The survey concludes that “by farming out management of operations that are not mission-critical, (these companies) are better able to concentrate on growth, competitors and profitability.&nbsp; If you’re not doing any outsourcing, you might be hurting your business”.
    <cite>Source: The Practical Guide to Successful Outsourcing (Owen Hartley) 2005</cite>
  </blockquote>
  <div class="abs photo" role="img" aria-label="Photo of business people shaking hands in an office"></div>

  <footer class="abs footer">
    <small>Copyright 2012 Tarlow HR Advisory</small>
    <nav><a href="#">Home</a>|<a href="#">Services</a>|<a href="#">Consultants</a>|<a href="#">Fees</a>|<a href="#">Contact Us</a></nav>
  </footer>
  <aside class="abs promo">
    <h2>Testimonials and<br>CV Referees</h2>
    <p>Availiable among request</p>
    <div class="promo-accent" role="img" aria-label="Decorative green ribbon graphic"></div>
  </aside>
</div>
</body>
</html>
```